Pebblemoor Supplements

Hi WP designers, this is my first time trying Pixel Bazaar ;-)

I would like a responsive woocommerce/wordpress theme for a company called Pebblemoor supplements. You can get an idea of what we sell, and how bad our old site is here:http://www.pebblemoorsupplements-example.com.sg/

Would love to see any type of modern looking design, a few guidelines:
- We've got a logo (see attached)
- We like green as a base for the colour scheme to match the logo but open to ideas

Target Market(s)

90% of customers will be Singaporean looking for good deals on top brands they already buy.

Industry/Entity Type

It Company

Font styles to use
Other font styles liked:
• Open Sans

Colors
9bcb3c
add136
cadf82
0492cd
eb1f27
a6459a
f78f20
ffc214

Requirements
Must have
• Sign In/Sign UpNewsletter sign up: best dealsFeatured deals sectionRatings/Reviews on products
Nice to have
• We're open to any ideas but would perhaps like to see something minimalist and easy on the eyes.
• Try to keep mostly images and white space
Should not have
• Too much text

```html
<!DOCTYPE html>
<html lang="en">
<head>
<meta charset="utf-8">
<title>Pebblemoor Supplements</title>
<link href="https://fonts.googleapis.com/css2?family=Open+Sans:ital,wght@0,400;0,600;0,700;1,400&display=swap" rel="stylesheet">
<style>
:root{
  --green:#9bcb3c;
  --green-mid:#add136;
  --green-soft:#cadf82;
  --green-dark:#3b5a14;
  --blue:#0492cd;
  --red:#eb1f27;
  --purple:#a6459a;
  --orange:#f78f20;
  --yellow:#ffc214;
  --panel:#f2f2f2;
  --line:#e0e0e0;
  --text:#333;
  --muted:#6b6b6b;
}
*{box-sizing:border-box;margin:0;padding:0}
html,body{width:733px;height:1200px;overflow:hidden}
body{position:relative;background:#fff;font-family:"Open Sans",sans-serif;color:var(--text)}
.abs{position:absolute}

/* top bar */
.topbar{left:0;top:0;width:733px;height:28px;background:var(--green)}
.toplinks{left:393px;top:8px;font-size:8px;color:#fff;display:flex;gap:9px}
.btn{position:absolute;font-size:8px;font-weight:700;color:#fff;text-align:center;line-height:18px;height:18px}
.btn-signin{left:535px;top:5px;width:47px;background:var(--yellow)}
.btn-signup{left:588px;top:5px;width:48px;background:var(--blue)}

/* header */
.header{left:0;top:28px;width:733px;height:60px;background:linear-gradient(#fff,#ececec)}
.brand{left:96px;top:53px;display:flex;align-items:center;gap:5px;font-size:9.5px;font-weight:600;color:#222;letter-spacing:.1px}
.brand-dot{width:8px;height:8px;border-radius:50%;background:var(--green)}
.nav{left:281px;top:52px;font-size:9.5px;font-weight:600;color:var(--green-dark)}
.nav span{position:absolute;white-space:nowrap}

/* hero */
.hero{left:0;top:88px;width:733px;height:245px;background:linear-gradient(180deg,#3f5f95 0%,#6f86b4 35%,#2a3a66 62%,#c6873a 72%,#1b2440 100%)}
.hero-title{left:0;top:118px;width:733px;text-align:center;color:#fff;font-size:14.5px;font-weight:600}
.hero-sub{left:0;top:140px;width:733px;text-align:center;color:#fff;font-size:12px}
.dots{left:341px;top:313px;display:flex;gap:7px}
.dots i{width:8px;height:8px;border-radius:50%;background:#fff;display:block}
.dots i.on{background:var(--green)}

/* section headers */
.sec-head{background:var(--green);color:#fff;font-size:7.5px;font-weight:700;padding-left:10px;display:flex;align-items:center}

/* categories */
.cats{left:98px;top:346px;width:125px}
.cats .sec-head{height:24px}
.cat{height:18px;background:var(--green-soft);border-bottom:1px solid #b9d466;color:#fff;font-size:7px;line-height:17px;padding-left:11px}
.cat::before{content:"›";margin-right:6px}

/* ratings */
.ratings{left:98px;top:674px;width:125px}
.ratings .sec-head{height:27px}
.ratings-box{height:230px;background:var(--panel);border:1px solid var(--line);position:relative}
.review{position:absolute;left:5px;display:flex;gap:5px}
.thumb{width:43px;height:41px;background:#fff}
.stars{color:var(--yellow);font-size:8px;letter-spacing:1px;line-height:10px;margin-top:4px}
.review b{display:block;color:var(--green);font-size:6.5px;line-height:10px}
.review small{display:block;font-size:6.5px;color:#222}

/* deals */
.deals-head{left:238px;width:398px;height:27px}
.deals-box{left:238px;width:398px;background:var(--panel);border:1px solid var(--line)}
.card{position:absolute;width:110px}
.card-img{height:79px;background:#fff;border:1px solid #e6e6e6;border-bottom:none}
.card-label{height:32px;background:var(--green);color:#fff;font-size:7px;font-weight:600;text-align:center;line-height:10px;padding-top:6px}
.card-btn{display:block;margin:7px auto 0;width:59px;height:14px;font-size:7px;font-weight:700;color:#fff;text-align:center;line-height:14px}
.add{background:var(--yellow)}
.buy{background:var(--purple);width:58px;height:15px;line-height:15px}
.view-more{left:238px;top:685px;width:398px;border-top:1px solid var(--line);text-align:center;font-size:7px;font-weight:700;color:#666;padding-top:11px}
.arrows{position:absolute;right:14px;font-size:10px;letter-spacing:2px}

/* partner names */
.partners-label{left:98px;top:956px;font-size:7.5px;font-style:italic;color:#555}
.partner{position:absolute;top:980px;height:42px;display:flex;align-items:center;justify-content:center;gap:5px;font-size:12px;font-weight:600;color:var(--muted)}
.partner::before{content:"";width:8px;height:8px;border-radius:50%;background:var(--green-soft)}

/* footer */
.footer{left:0;top:1041px;width:733px;height:159px;background:var(--green);color:#fff}
.fcol{position:absolute;top:26px;font-size:7.5px}
.fcol h4{font-size:7.5px;font-weight:700;margin-bottom:8px}
.fcol li{list-style:none;font-weight:600;line-height:16.8px}
.testimonial p{font-size:7px;line-height:13.6px;width:160px}
.testimonial strong{display:block;margin-top:4px;font-size:7px}
.field{position:absolute;left:477px;width:159px;height:19px;background:var(--green-soft);color:#fff;font-size:6.5px;line-height:19px;padding-left:8px}
.subscribe{position:absolute;left:477px;top:92px;width:58px;height:20px;background:var(--blue);font-size:6.5px;font-weight:700;line-height:20px;text-align:center}
.copyright{position:absolute;left:97px;top:137px;font-size:6.5px;font-weight:600}
.social{position:absolute;left:595px;top:135px;display:flex;gap:3px}
.social i{width:11px;height:11px;border-radius:50%;display:block}
</style>
</head>
<body>

<div class="abs topbar"></div>
<div class="abs toplinks"><span>Account</span><span>|</span><span>Basket</span><span>|</span><span>Checkout</span></div>
<div class="btn btn-signin">SIGN IN</div>
<div class="btn btn-signup">SIGN UP</div>

<div class="abs header"></div>
<div class="abs brand"><span class="brand-dot"></span>PEBBLEMOOR SUPPLEMENTS</div>
<nav class="abs nav">
  <span style="left:0">Home</span>
  <span style="left:43px">About Us</span>
  <span style="left:99px">Products</span>
  <span style="left:155px">Online Shop</span>
  <span style="left:225px">Store</span>
  <span style="left:265px">FAQ's</span>
  <span style="left:306px">Contact Us</span>
</nav>

<div class="abs hero" role="img" aria-label="City skyline at dusk with a lit bridge over the river"></div>
<div class="abs hero-title">Pebblemoor Supplements</div>
<div class="abs hero-sub">Bringing you australia's finest vitamins rights to your door step</div>
<div class="abs dots"><i class="on"></i><i></i><i></i><i></i></div>

<aside class="abs cats">
  <div class="sec-head">CATEGORIES</div>
  <div class="cat">Antioxidants</div><div class="cat">Brain Health</div><div class="cat">Cardiovascular</div>
  <div class="cat">Digestive Health</div><div class="cat">Energy Support</div><div class="cat">Essential Fatty Acids</div>
  <div class="cat">Immune Health</div><div class="cat">Joint Health</div><div class="cat">Kids</div>
  <div class="cat">Men</div><div class="cat">Minerals</div><div class="cat">Natural</div>
  <div class="cat">Reproductive Health</div><div class="cat">Sleep</div><div class="cat">Vitamins</div>
  <div class="cat">Women</div>
</aside>

<aside class="abs ratings">
  <div class="sec-head">RATINGS/REVIEWS</div>
  <div class="ratings-box">
    <div class="review" style="top:12px"><div class="thumb" role="img" aria-label="Fish oil product box" style="background:radial-gradient(#6cc7c4 30%,#fff 65%)"></div><div><div class="stars">★★★★★</div><b>Ridgeway Fish Oil</b><small>1000mg , Caps 400</small></div></div>
    <div class="review" style="top:67px"><div class="thumb" role="img" aria-label="Fish oil bottle" style="background:radial-gradient(#e8a357 30%,#fff 65%)"></div><div><div class="stars">★★★★★</div><b>Ridgeway Fish Oil</b><small>1000mg , Caps 400</small></div></div>
    <div class="review" style="top:122px"><div class="thumb" role="img" aria-label="Fish oil bottle" style="background:radial-gradient(#c8672a 30%,#fff 65%)"></div><div><div class="stars">★★★★★</div><b>Ridgeway Fish Oil</b><small>1000mg , Caps 400</small></div></div>
    <div class="review" style="top:177px"><div class="thumb" role="img" aria-label="Fish oil bottle" style="background:radial-gradient(#2f7a3a 30%,#fff 65%)"></div><div><div class="stars">★★★★★</div><b>Ridgeway Fish Oil</b><small>1000mg , Caps 400</small></div></div>
  </div>
</aside>

<div class="abs sec-head deals-head" style="top:346px;padding-left:15px">FEATURED DEALS</div>
<div class="abs deals-box" style="top:378px;height:339px"></div>
<div class="card" style="left:252px;top:392px"><div class="card-img" role="img" aria-label="CoQ10 supplement bottle" style="background:radial-gradient(#9b2a2a 25%,#fff 58%)"></div><div class="card-label">Ridgeway CoQ10<br>150mg Caps 30</div><span class="card-btn add">Add To Cart</span></div>
<div class="card" style="left:382px;top:392px"><div class="card-img" role="img" aria-label="Evening primrose oil bottle" style="background:radial-gradient(#4aa3a8 25%,#fff 58%)"></div><div class="card-label">Ridgeway CoQ10<br>150mg Caps 30</div><span class="card-btn add">Add To Cart</span></div>
<div class="card" style="left:511px;top:392px"><div class="card-img" role="img" aria-label="Multivitamin bottle" style="background:radial-gradient(#2a3d8a 25%,#fff 58%)"></div><div class="card-label">Ridgeway CoQ10<br>150mg Caps 30</div><span class="card-btn add">Add To Cart</span></div>
<div class="card" style="left:252px;top:534px"><div class="card-img" role="img" aria-label="Fish oil tub" style="background:radial-gradient(#1f6f5a 25%,#fff 58%)"></div><div class="card-label">Ridgeway CoQ10<br>150mg Caps 30</div><span class="card-btn add">Add To Cart</span></div>
<div class="card" style="left:382px;top:534px"><div class="card-img" role="img" aria-label="Kids omega-3 box" style="background:radial-gradient(#e6c12a 25%,#fff 58%)"></div><div class="card-label">Ridgeway CoQ10<br>150mg Caps 30</div><span class="card-btn add">Add To Cart</span></div>
<div class="card" style="left:511px;top:534px"><div class="card-img" role="img" aria-label="Fish oil bottle" style="background:radial-gradient(#1f7a3e 25%,#fff 58%)"></div><div class="card-label">Ridgeway CoQ10<br>150mg Caps 30</div><span class="card-btn add">Add To Cart</span></div>
<div class="abs view-more">VIEW MORE DEALS</div>

<div class="abs sec-head deals-head" style="top:734px;padding-left:15px">BEST DEAL<span class="arrows">‹ ›</span></div>
<div class="abs deals-box" style="top:768px;height:163px"></div>
<div class="card" style="left:252px;top:782px"><div class="card-img" role="img" aria-label="Glucosamine tub" style="background:radial-gradient(#c9303a 25%,#fff 58%)"></div><div class="card-label">Ridgeway CoQ10<br>150mg Caps 30</div><span class="card-btn buy">BUY NOW</span></div>
<div class="card" style="left:382px;top:782px"><div class="card-img" role="img" aria-label="Omega supplement bottle" style="background:radial-gradient(#2e7f9a 25%,#fff 58%)"></div><div class="card-label">Ridgeway CoQ10<br>150mg Caps 30</div><span class="card-btn buy">BUY NOW</span></div>
<div class="card" style="left:511px;top:782px"><div class="card-img" role="img" aria-label="Fish oil tub" style="background:radial-gradient(#e8d24a 25%,#fff 58%)"></div><div class="card-label">Ridgeway CoQ10<br>150mg Caps 30</div><span class="card-btn buy">BUY NOW</span></div>

<div class="abs partners-label">Company Logos *</div>
<div class="partner" style="left:98px;width:86px">Alpenvale</div>
<div class="partner" style="left:208px;width:98px">Fortune Vital</div>
<div class="partner" style="left:320px;width:72px">Wildroot</div>
<div class="partner" style="left:410px;width:120px">Ridgeway</div>
<div class="partner" style="left:548px;width:90px">Calloway</div>

<footer class="abs footer">
  <div class="fcol" style="left:97px"><h4>Quick Links</h4><ul><li>Home</li><li>About Us</li><li>Products</li><li>FAQ's</li><li>Contact Us</li></ul></div>
  <div class="fcol" style="left:182px"><h4>Other Links</h4><ul><li>Privacy Policy</li><li>Terms &amp; Conditions</li><li>Promotions</li><li>Site Map</li></ul></div>
  <div class="fcol testimonial" style="left:283px"><h4>Testimonials <span style="margin-left:100px;font-weight:400">‹ ›</span></h4><p>Tried it out.. shipping arrived at doorstep as stated and items in good condition. Prices are also cheap. Will continue shopping from this site.....</p><strong>• Tan Mei Ling - Woodlands</strong></div>
  <div class="fcol" style="left:476px"><h4>Newsletter Sign Up</h4></div>
  <div class="field" style="top:46px">Name</div>
  <div class="field" style="top:69px">E-Mail ID</div>
  <div class="subscribe">SUBSCRIBE</div>
  <div class="copyright">© 2014 COMPANY NAME ,ALL RIGHTS RESERVED &nbsp;| TERMS OF SERVICE &nbsp;| &nbsp;PRIVACY POLICY</div>
  <div class="social"><i style="background:#3fb0e0"></i><i style="background:#2d5aa0"></i><i style="background:#1a6fa8"></i></div>
</footer>

</body>
</html>
```